Brickline Rentals podcast postcard

I've launched a podcast about apartment investing, ownership and management which is newly up on orbix and wavlino. I want to create a postcard that I can mail to my client base to get them to subscribe

```html
<!DOCTYPE html>
<html lang="en">
<head>
<meta charset="utf-8">
<title>Brickline Rentals Postcard</title>
<link href="https://fonts.googleapis.com/css2?family=Montserrat:wght@400;500;600;700;800&display=swap" rel="stylesheet">
<style>
  :root {
    --navy: #3a2f6e;
    --green: #4e9a2f;
    --white: #ffffff;
    --page: #f2f2f2;
    --ink: #3a2f6e;
    --line: #c9c9c9;
    --stamp: #e4e4e4;
    --sky-top: #8fb7dc;
    --sky-bottom: #5d7d98;
    --room-a: #8a7a6a;
    --room-b: #d8d0c4;
  }
  * { margin: 0; padding: 0; box-sizing: border-box; }
  html, body { width: 1200px; height: 2272px; overflow: hidden; }
  body { background: var(--page); font-family: "Montserrat", sans-serif; position: relative; }

  .postcard {
    position: absolute; left: 80px; width: 1040px; height: 700px;
    background: var(--white); overflow: hidden;
    box-shadow: 0 6px 24px rgba(0,0,0,.18);
  }
  .postcard--front { top: 250px; }
  .postcard--back { top: 1250px; }
  .postcard__shapes { position: absolute; inset: 0; width: 1040px; height: 700px; }

  .brand { position: absolute; display: flex; align-items: center; gap: 12px; }
  .brand__dot { width: 46px; height: 46px; border-radius: 50%; background: var(--green); }
  .brand__name { color: var(--green); font-weight: 700; font-size: 22px; line-height: 1.05; letter-spacing: .5px; text-transform: uppercase; }

  .front__title {
    position: absolute; left: 40px; top: 150px; color: var(--white);
    font-weight: 800; font-size: 62px; line-height: 1.05; text-transform: uppercase;
  }
  .front__rule { position: absolute; left: 40px; top: 300px; width: 440px; height: 2px; background: rgba(255,255,255,.35); }
  .services { position: absolute; left: 40px; top: 325px; list-style: none; }
  .services li { display: flex; align-items: center; gap: 18px; color: var(--white); font-size: 32px; font-weight: 500; letter-spacing: 1px; height: 64px; }
  .services svg { width: 46px; height: 46px; flex: none; }

  .contact { position: absolute; color: var(--white); }
  .contact__phone { display: flex; align-items: center; gap: 10px; font-weight: 700; }
  .contact__web { font-weight: 500; }
  .front__contact { left: 40px; top: 590px; }
  .front__contact .contact__phone { font-size: 40px; }
  .front__contact .contact__web { font-size: 24px; margin-left: 4px; }

  .photo { position: absolute; }

  .back__title { position: absolute; left: 36px; top: 34px; color: var(--white); font-size: 36px; font-weight: 500; text-transform: uppercase; letter-spacing: .5px; }
  .back__body { position: absolute; left: 36px; top: 92px; width: 470px; color: var(--white); font-size: 14px; line-height: 1.5; }
  .checklist { position: absolute; left: 36px; top: 250px; width: 470px; display: grid; grid-template-columns: 1fr 1fr; row-gap: 18px; column-gap: 20px; list-style: none; }
  .checklist li { display: flex; align-items: center; gap: 10px; color: var(--white); font-size: 14px; }
  .checklist svg { width: 18px; height: 18px; flex: none; }
  .back__contact { left: 36px; top: 570px; }
  .back__contact .contact__phone { font-size: 38px; }
  .back__contact .contact__web { font-size: 23px; margin-left: 4px; }

  .stamp { position: absolute; left: 880px; top: 40px; width: 110px; height: 125px; background: var(--stamp); }
  .address-line { position: absolute; left: 640px; width: 350px; height: 2px; background: var(--line); }
</style>
</head>
<body>

<section class="postcard postcard--front">
  <svg class="postcard__shapes" viewBox="0 0 1040 700" aria-hidden="true">
    <polygon points="0,120 603,120 543,540 0,540" fill="var(--navy)"/>
    <polygon points="620,0 648,0 548,700 520,700" fill="var(--green)"/>
    <polygon points="0,585 536,585 522,680 0,680" fill="var(--green)"/>
  </svg>
  <svg class="photo" style="left:0;top:0" width="1040" height="700" viewBox="0 0 1040 700" role="img" aria-label="Photo of tall apartment towers against a blue sky">
    <defs>
      <linearGradient id="sky" x1="0" y1="0" x2="0" y2="1">
        <stop offset="0" stop-color="var(--sky-top)"/>
        <stop offset="1" stop-color="var(--sky-bottom)"/>
      </linearGradient>
    </defs>
    <polygon points="648,0 1040,0 1040,700 548,700" fill="url(#sky)"/>
  </svg>

  <div class="brand" style="left:40px;top:32px">
    <span class="brand__dot"></span>
    <span class="brand__name">Brickline<br>Rentals</span>
  </div>

  <h1 class="front__title">Brickline<br>Rentals</h1>
  <div class="front__rule"></div>
  <ul class="services">
    <li><svg viewBox="0 0 46 46"><circle cx="23" cy="23" r="22" fill="var(--green)"/><path d="M14 24l6 6 12-13" stroke="#fff" stroke-width="4" fill="none" stroke-linecap="round" stroke-linejoin="round"/></svg>INVESTING</li>
    <li><svg viewBox="0 0 46 46"><circle cx="23" cy="23" r="22" fill="var(--green)"/><path d="M14 24l6 6 12-13" stroke="#fff" stroke-width="4" fill="none" stroke-linecap="round" stroke-linejoin="round"/></svg>OWNING</li>
    <li><svg viewBox="0 0 46 46"><circle cx="23" cy="23" r="22" fill="var(--green)"/><path d="M14 24l6 6 12-13" stroke="#fff" stroke-width="4" fill="none" stroke-linecap="round" stroke-linejoin="round"/></svg>MANAGING</li>
  </ul>

  <div class="contact front__contact">
    <div class="contact__phone">
      <svg width="34" height="34" viewBox="0 0 24 24" aria-hidden="true"><path fill="#fff" d="M6.6 10.8a15.1 15.1 0 0 0 6.6 6.6l2.2-2.2c.3-.3.7-.4 1-.2 1.1.4 2.3.6 3.6.6.6 0 1 .4 1 1V20c0 .6-.4 1-1 1A17 17 0 0 1 3 4c0-.6.4-1 1-1h3.5c.6 0 1 .4 1 1 0 1.3.2 2.5.6 3.6.1.3 0 .7-.2 1z"/></svg>
      1234-567-890
    </div>
    <div class="contact__web">www.website.com</div>
  </div>
</section>

<section class="postcard postcard--back">
  <svg class="postcard__shapes" viewBox="0 0 1040 700" aria-hidden="true">
    <polygon points="0,0 565,0 508,410 0,410" fill="var(--navy)"/>
    <polygon points="0,560 484,560 470,662 0,662" fill="var(--green)"/>
  </svg>
  <svg class="photo" style="left:0;top:0" width="1040" height="700" viewBox="0 0 1040 700" role="img" aria-label="Photo of a furnished apartment living room">
    <defs>
      <linearGradient id="room" x1="0" y1="0" x2="1" y2="0">
        <stop offset="0" stop-color="var(--room-a)"/>
        <stop offset="1" stop-color="var(--room-b)"/>
      </linearGradient>
    </defs>
    <polygon points="0,420 506,420 491,548 0,548" fill="url(#room)"/>
  </svg>

  <h2 class="back__title">Brickline Rentals</h2>
  <p class="back__body">Our new podcast covers apartment investing, ownership and property management. Each episode brings practical tips from owners and managers who have done the work. Listen now on orbix and wavlino, subscribe for weekly episodes, and share it with anyone planning their next rental property.</p>
  <ul class="checklist">
    <li><svg viewBox="0 0 18 18"><circle cx="9" cy="9" r="8" fill="none" stroke="#fff" stroke-width="1.5"/><path d="M5 9.5l2.5 2.5 5-5.5" stroke="#fff" stroke-width="1.8" fill="none"/></svg>Find a good deal</li>
    <li><svg viewBox="0 0 18 18"><circle cx="9" cy="9" r="8" fill="none" stroke="#fff" stroke-width="1.5"/><path d="M5 9.5l2.5 2.5 5-5.5" stroke="#fff" stroke-width="1.8" fill="none"/></svg>Finance your buy</li>
    <li><svg viewBox="0 0 18 18"><circle cx="9" cy="9" r="8" fill="none" stroke="#fff" stroke-width="1.5"/><path d="M5 9.5l2.5 2.5 5-5.5" stroke="#fff" stroke-width="1.8" fill="none"/></svg>Screen new tenants</li>
    <li><svg viewBox="0 0 18 18"><circle cx="9" cy="9" r="8" fill="none" stroke="#fff" stroke-width="1.5"/><path d="M5 9.5l2.5 2.5 5-5.5" stroke="#fff" stroke-width="1.8" fill="none"/></svg>Set fair rents</li>
    <li><svg viewBox="0 0 18 18"><circle cx="9" cy="9" r="8" fill="none" stroke="#fff" stroke-width="1.5"/><path d="M5 9.5l2.5 2.5 5-5.5" stroke="#fff" stroke-width="1.8" fill="none"/></svg>Handle repairs fast</li>
    <li><svg viewBox="0 0 18 18"><circle cx="9" cy="9" r="8" fill="none" stroke="#fff" stroke-width="1.5"/><path d="M5 9.5l2.5 2.5 5-5.5" stroke="#fff" stroke-width="1.8" fill="none"/></svg>Grow your portfolio</li>
  </ul>

  <div class="contact back__contact">
    <div class="contact__phone">
      <svg width="32" height="32" viewBox="0 0 24 24" aria-hidden="true"><path fill="#fff" d="M6.6 10.8a15.1 15.1 0 0 0 6.6 6.6l2.2-2.2c.3-.3.7-.4 1-.2 1.1.4 2.3.6 3.6.6.6 0 1 .4 1 1V20c0 .6-.4 1-1 1A17 17 0 0 1 3 4c0-.6.4-1 1-1h3.5c.6 0 1 .4 1 1 0 1.3.2 2.5.6 3.6.1.3 0 .7-.2 1z"/></svg>
      1234-567-890
    </div>
    <div class="contact__web">www.website.com</div>
  </div>

  <div class="brand" style="left:620px;top:48px">
    <span class="brand__dot" style="width:38px;height:38px"></span>
    <span class="brand__name" style="font-size:18px">Brickline<br>Rentals</span>
  </div>
  <div class="stamp"></div>
  <div class="address-line" style="top:320px"></div>
  <div class="address-line" style="top:380px"></div>
  <div class="address-line" style="top:440px"></div>
</section>

</body>
</html>
```